Hot sauce company needs a logo and label design- simple, clean & fresh

Toby K's a hot pepper sauce company based on the edge of London needs a logo and label design .
The sauces are handmade in small batches with natural ingredients , no added sugars or extracts and so we would like a clean fresh label to reflect this - avoiding all the macho devil and flames novelty stuff.
At present there are four sauces - Jalapeno ,Chipotle,Habanero and Reaper we would like to have one Toby K's label with the name of the sauce being changeable allowing us to react to what ingredients are available .
Updates

Project Deadline Extended
Reason: Hi Guys I have received a few requests to extend the deadline on the project and so I am thanks Toby K's

Target Market(s)

people who care what they eat

Industry/Entity Type

Food Store

Logo Text

Toby K's handmade hot sauce

Requirements
Must have
• Toby K's handmade hot sauce - or the logo
• the name of the sauce ie jalapeno
• no added sugars
Nice to have
• handmade
• small batch
Should not have
• cartoon men with smoke coming out of their ears
• devils and the flames of hell

```html
<!DOCTYPE html>
<html lang="en">
<head>
<meta charset="utf-8">
<title>Toby K's Reaper – Label</title>
<link rel="stylesheet" href="https://fonts.googleapis.com/css2?family=Cabin:wght@500;600;700&display=swap">
<style>
  :root {
    --page-bg: #f4f4f4;
    --label-red: #e8413f;
    --label-red-light: #f0625c;
    --label-red-deep: #d9302f;
    --frame-olive: #a8ad4a;
    --panel-white: #fbfbf8;
    --ink-dark: #2b2a2c;
    --ink-maroon: #7a1d22;
  }
  * { margin: 0; padding: 0; box-sizing: border-box; }
  html, body {
    width: 1200px;
    height: 1000px;
    overflow: hidden;
    background: var(--page-bg);
    font-family: "Cabin", "Helvetica Neue", Arial, sans-serif;
  }
  .canvas {
    position: relative;
    width: 1200px;
    height: 1000px;
  }
  .label {
    position: absolute;
    left: 330px;
    top: 70px;
    width: 540px;
    height: 860px;
  }
  .label-art {
    position: absolute;
    inset: 0;
    width: 100%;
    height: 100%;
  }
  .label-copy {
    position: absolute;
    inset: 0;
    display: flex;
    flex-direction: column;
    align-items: center;
    text-align: center;
  }
  .brand {
    margin-top: 268px;
    display: flex;
    align-items: center;
    gap: 12px;
    font-weight: 700;
    font-size: 40px;
    color: var(--ink-maroon);
    letter-spacing: 1px;
  }
  .brand-dot {
    width: 22px;
    height: 22px;
    border-radius: 50%;
    background: var(--label-red);
  }
  .sauce-name {
    margin-top: 62px;
    font-weight: 600;
    font-size: 78px;
    letter-spacing: 2px;
    color: var(--ink-dark);
  }
  .claims {
    margin-top: 44px;
    font-weight: 500;
    font-size: 30px;
    line-height: 1.4;
    color: var(--ink-maroon);
  }
  .sugar-note {
    margin-top: 38px;
    font-weight: 500;
    font-size: 20px;
    color: var(--ink-maroon);
  }
</style>
</head>
<body>
<main class="canvas">
  <section class="label">
    <svg class="label-art" viewBox="0 0 540 860" aria-hidden="false">
      <defs>
        <radialGradient id="ray-glow" cx="50%" cy="45%" r="70%">
          <stop offset="0%" stop-color="var(--label-red-light)"/>
          <stop offset="100%" stop-color="var(--label-red-deep)"/>
        </radialGradient>
      </defs>
      <rect class="label-ground" width="540" height="860" fill="url(#ray-glow)" role="img" aria-label="Red background with fine sunburst rays radiating from the centre"/>
      <polygon class="diamond-frame" points="270,12 532,430 270,848 8,430" fill="var(--frame-olive)"/>
      <polygon class="diamond-panel" points="270,34 518,430 270,826 22,430" fill="var(--panel-white)"/>
    </svg>
    <div class="label-copy">
      <div class="brand"><span class="brand-dot"></span>Toby K's</div>
      <h1 class="sauce-name">REAPER</h1>
      <p class="claims">Small batch<br>Handmade</p>
      <p class="sugar-note">no added sugars</p>
    </div>
  </section>
</main>
</body>
</html>
```